Lantern Hearthworks Business Cards

Looking to create simple business cards that highlight our unique three sided triangle fire pit design with the colors and font of our logo, listed below.

Requirements
Must have
• Looking for something simple that includes a picture of our fire pit with name, website (lanternhearthworks.com), phone number and email. Want to keep the color mostly orange and black.
• Font is gotham(medium) and orange color code is #ee6e22

```html
<!DOCTYPE html>
<html lang="en">
<head>
<meta charset="utf-8">
<title>Lantern Hearthworks Business Cards</title>
<link rel="stylesheet" href="https://fonts.googleapis.com/css2?family=Montserrat:wght@500;600&family=Source+Sans+3:wght@400&display=swap">
<style>
  :root {
    --backdrop: #e0dcd6;
    --card: #ffffff;
    --ember: #ee6e22;
    --flame: #ef8222;
    --glow: #f29d50;
    --charcoal: #6d6e71;
  }
  * { box-sizing: border-box; margin: 0; padding: 0; }
  html, body {
    width: 1200px;
    height: 1006px;
    overflow: hidden;
    background: var(--backdrop);
  }
  .sheet {
    position: relative;
    width: 1200px;
    height: 1006px;
  }
  .card {
    position: absolute;
    left: 280px;
    width: 613px;
    height: 358px;
    background: var(--card);
    overflow: hidden;
  }
  .card--front { top: 92px; }
  .card--back { top: 541px; }

  .brand-name {
    position: absolute;
    left: 0;
    right: 0;
    top: 50%;
    transform: translateY(-50%);
    text-align: center;
    font-family: "Montserrat", sans-serif;
    font-weight: 500;
    color: var(--ember);
    font-size: 33px;
    line-height: 1.05;
    letter-spacing: 0.14em;
    text-transform: uppercase;
  }
  .brand-name span { display: block; }

  .holder {
    position: absolute;
    left: 59px;
    top: 50px;
    font-family: "Montserrat", sans-serif;
  }
  .holder__name {
    font-weight: 600;
    font-size: 30px;
    color: var(--charcoal);
    line-height: 1.1;
  }
  .holder__position {
    font-weight: 600;
    font-size: 23px;
    color: var(--ember);
    letter-spacing: 0.02em;
    margin-top: 2px;
  }

  .contact {
    position: absolute;
    left: 52px;
    top: 198px;
    list-style: none;
    font-family: "Source Sans 3", sans-serif;
    font-size: 22px;
    color: var(--charcoal);
  }
  .contact__row {
    display: flex;
    align-items: center;
    height: 33px;
  }
  .contact__icon {
    width: 20px;
    height: 20px;
    margin-right: 25px;
    flex: none;
  }
  .contact__icon path,
  .contact__icon circle,
  .contact__icon rect { fill: var(--ember); }

  .accent-panel {
    position: absolute;
    top: 0;
    right: 0;
    width: 170px;
    height: 358px;
    background: linear-gradient(180deg, var(--ember) 0%, var(--flame) 50%, var(--glow) 100%);
  }
</style>
</head>
<body>
<main class="sheet">
  <section class="card card--front" aria-label="Card front">
    <h1 class="brand-name"><span>Lantern</span><span>Hearthworks</span></h1>
  </section>

  <section class="card card--back" aria-label="Card back">
    <div class="accent-panel" role="img" aria-label="Layered orange flame-wave decoration"></div>

    <div class="holder">
      <p class="holder__name">Name</p>
      <p class="holder__position">POSITION</p>
    </div>

    <ul class="contact">
      <li class="contact__row">
        <svg class="contact__icon" viewBox="0 0 20 20" aria-label="Email"><path d="M1 2 L19 11 L7 12 L6 17 L5 11 Z"/></svg>
        hello@lanternhearthworks.com
      </li>
      <li class="contact__row">
        <svg class="contact__icon" viewBox="0 0 20 20" aria-label="Phone"><path d="M1 7 C4 3 16 3 19 7 L17 9 L14 7 V9 H6 V7 L3 9 Z"/><rect x="2" y="10" width="16" height="8" rx="1"/></svg>
        0123456789
      </li>
      <li class="contact__row">
        <svg class="contact__icon" viewBox="0 0 20 20" aria-label="Website"><circle cx="10" cy="10" r="9"/></svg>
        lanternhearthworks.com
      </li>
    </ul>
  </section>
</main>
</body>
</html>
```